Pivots & Treads .com

This website is simple!!!
Landing page background image should capture the customers attention!!! We will provide a image as a example of what we like. The purpose for this website is to provide customers with a clean easy way to request a quote for industrial casters and wheels by OEM’s as well as maintenance departments worldwide. Please see if you can follow our thought process below.
Customer comes to website, they are invited to Request a Quote by providing us with Manufacturer Name, Manufacturers Part # and quantity needed.
If this is not known the customer will complete will WP conversation format form answering about 10 questions
Or
Look up the part number in one of the 8 to 12 catalogs located in the Flippin Book format on our catalog page, or equal plug in .
When the client request a quote a account page will pop up request The following:
Clients first and last name
Email address
And optional questions
Company name and best contact number.
Once this is complete customer will hit SUBMIT.
The customers request will be in system. A email will be sent to Customer service notifying us the Quote Request has been made.
We will then build a quote for the customer with a good, better and best options. Customers Request a Quote submission may have more than one caster or wheel requested at a time, so website must allow this.
When the customer comes back into website there email address will come up as the account name and request a password be made for them. This will allow them to store quotes in their account for future needs. If quote is older than 30 day the system will trigger a button at the bottom of the quote for resubmit Request for updated quote.
Once customer reviews quote the quote can be Converted to order within the website.
Once Converted the system will send us a email and order will be processed.
We will need a Chat program that will text to CS the questions.
You will need to have high quality graphic design skills on your team.
We have found 2 plugins that would work nicely with our new website Flippin books to showcase our catalogs for customers to research and WPForms conversation forms to complete request for quote form.
Just Ideas:
Very very ghosted caster blueprint in white background but very very ghosted or the icon just idea
We have never had a font used we like
Grayscale every except for rubber on wheels and logo icon
Website should have hamburger menu on left
Website should hav responsive deign
Account head on right side
Has anyone read the brief from top to bottom and the updates, I’m seeing a lot of duplicates of the website I posted in images I want a clean website With lite backgrand with the poly being definite colors on each wheel I added a green yellow and red image has anyone looked at that Just a question?
Went on vacation/holiday

```html
<!DOCTYPE html>
<html lang="en">
<head>
<meta charset="utf-8">
<title>Pivots &amp; Treads .com – Quote Flow</title>
<link rel="stylesheet" href="https://fonts.googleapis.com/css2?family=Montserrat:wght@300;400;500;600;700&family=Poppins:wght@400;500&display=swap">
<style>
  :root {
    --board: #c8c8c8;
    --brand: #3a51a3;
    --brand-deep: #2a3f8e;
    --navy: #1f2f78;
    --night: #1c2757;
    --bright: #2d6cf2;
    --ink: #2d2d2d;
    --muted: #6b6b6b;
    --paper: #ffffff;
    --mist: #efefef;
    --fog: #e8e8e8;
    --field: #e9ebf4;
    --ok: #4aa81c;
  }
  * { box-sizing: border-box; margin: 0; padding: 0; }
  html, body { width: 776px; height: 1200px; overflow: hidden; }
  body { background: var(--board); font-family: "Poppins", sans-serif; color: var(--ink); position: relative; }
  .abs { position: absolute; }
  .step-label { position: absolute; font-family: "Montserrat", sans-serif; font-weight: 300; font-size: 22px; color: #111; letter-spacing: .5px; text-align: center; width: 120px; }

  .panel { position: absolute; overflow: hidden; }
  .home { left: 43px; top: 62px; width: 321px; height: 1075px; background: var(--paper); }

  .center { left: 0; right: 0; text-align: center; }
  .icon-btn { position: absolute; width: 14px; height: 14px; border: .8px solid rgba(255,255,255,.85); border-radius: 3px; }
  .icon-btn svg { width: 100%; height: 100%; display: block; }
  .brand-dot { position: absolute; border-radius: 50%; background: #fff; }
  .brand-name { position: absolute; font-family: "Montserrat", sans-serif; font-weight: 600; font-size: 7px; color: #fff; letter-spacing: .1px; white-space: nowrap; }

  /* hero */
  .hero { left: 0; top: 0; width: 321px; height: 181px; background: radial-gradient(ellipse at 45% 70%, #5b6db0 0%, #4358a8 40%, var(--brand) 75%); }
  .hero-kicker { position: absolute; top: 81px; font-family: "Montserrat", sans-serif; font-weight: 600; font-size: 6.4px; color: #fff; }
  .hero-title { position: absolute; top: 92px; font-family: "Montserrat", sans-serif; font-weight: 700; font-size: 12px; color: #fff; }
  .field { position: absolute; height: 12px; background: var(--field); border-radius: 2.5px; font-size: 3.6px; color: #555; line-height: 12px; padding-left: 4px; }
  .field.select::after { content: ""; position: absolute; right: 4px; top: 4.5px; width: 2px; height: 2px; border-right: .6px solid #555; border-bottom: .6px solid #555; transform: rotate(45deg); }
  .btn-bright { position: absolute; height: 12px; background: var(--bright); border-radius: 2.5px; color: #fff; font-family: "Montserrat", sans-serif; font-weight: 600; font-size: 4px; line-height: 12px; padding-left: 4px; box-shadow: 0 1px 2px rgba(0,0,0,.25); }
  .btn-bright svg { position: absolute; right: 3px; top: 4.5px; width: 9px; height: 3px; }

  /* about */
  .about-photo { left: 0; top: 181px; width: 190px; height: 132px; background: linear-gradient(90deg, #8a8e98 0%, #a9acb3 45%, rgba(255,255,255,0) 100%); }
  .section-title { position: absolute; font-family: "Montserrat", sans-serif; font-weight: 700; font-size: 8.4px; line-height: 10px; color: var(--brand); }
  .copy { position: absolute; font-size: 3.7px; line-height: 4.9px; color: #555; }
  .btn-navy { position: absolute; height: 16px; background: var(--navy); border-radius: 3px; color: #fff; font-family: "Montserrat", sans-serif; font-weight: 600; font-size: 4.1px; line-height: 16px; text-align: center; box-shadow: 0 1px 2px rgba(0,0,0,.3); }
  .btn-blue { position: absolute; height: 16px; background: var(--bright); border-radius: 3px; color: #fff; font-family: "Montserrat", sans-serif; font-weight: 600; font-size: 4.1px; line-height: 16px; text-align: center; box-shadow: 0 1px 2px rgba(0,0,0,.3); }

  .looking { left: 0; top: 313px; width: 321px; height: 114px; background: var(--mist); }

  .steps { left: 0; top: 427px; width: 321px; height: 138px; background: radial-gradient(ellipse at 50% 60%, #4e61ab 0%, var(--brand) 70%); }
  .steps-kicker { position: absolute; top: 22px; font-family: "Montserrat", sans-serif; font-weight: 600; font-size: 4.6px; color: #fff; }
  .steps-title { position: absolute; top: 32px; font-family: "Montserrat", sans-serif; font-weight: 700; font-size: 8.2px; color: #fff; }

  .products-title { position: absolute; top: 585px; font-family: "Montserrat", sans-serif; font-weight: 700; font-size: 10px; color: var(--brand); }
  .products-copy { position: absolute; top: 602px; left: 70px; width: 181px; text-align: center; font-size: 3.6px; line-height: 4.9px; color: #555; }
  .card { position: absolute; width: 56px; height: 72px; background: #f6f6f6; border: .5px solid #e2e2e2; }
  .card-photo { position: absolute; left: 0; top: 0; width: 100%; height: 48px; background: radial-gradient(circle at 50% 50%, #6d737c 0%, #9aa0a8 30%, #ffffff 62%); }
  .card-name { position: absolute; top: 54px; left: 0; right: 0; text-align: center; font-family: "Montserrat", sans-serif; font-weight: 600; font-size: 3.8px; color: #666; }
  .card-meta { position: absolute; top: 61px; left: 0; right: 0; text-align: center; font-size: 3.1px; color: #888; }

  .services-title { position: absolute; top: 797px; font-family: "Montserrat", sans-serif; font-weight: 700; font-size: 10px; color: var(--brand); }
  .service-photo { position: absolute; top: 819px; width: 98px; height: 94px; }
  .service-name { position: absolute; top: 918px; width: 98px; text-align: center; font-family: "Montserrat", sans-serif; font-weight: 600; font-size: 5.8px; color: #333; }
  .service-copy { position: absolute; top: 929px; width: 98px; text-align: center; font-size: 3.3px; line-height: 4.2px; color: #666; }

  .footer { left: 0; top: 952px; width: 321px; height: 103px; background: var(--fog); }
  .foot-head { position: absolute; top: 27px; font-family: "Montserrat", sans-serif; font-weight: 600; font-size: 6px; color: #222; }
  .foot-links { position: absolute; top: 42px; left: 119px; list-style: none; font-size: 3.4px; line-height: 6px; color: #333; }
  .foot-line { position: absolute; font-size: 3.4px; line-height: 4.6px; color: #333; }
  .foot-pin { position: absolute; width: 10px; height: 10px; border-radius: 50%; background: var(--brand); }
  .foot-pin svg { width: 100%; height: 100%; display: block; }
  .newsletter { position: absolute; left: 236px; top: 59px; width: 63px; height: 11px; background: #fff; border-radius: 6px; font-family: "Montserrat", sans-serif; font-size: 3.6px; line-height: 11px; padding-left: 5px; color: #555; box-shadow: 0 .5px 1.5px rgba(0,0,0,.15); }
  .newsletter svg { position: absolute; right: .5px; top: .5px; width: 10px; height: 10px; }
  .social { position: absolute; top: 77px; width: 9px; height: 9px; border-radius: 50%; border: .6px solid #333; }
  .legal { left: 0; top: 1055px; width: 321px; height: 20px; background: var(--brand-deep); color: #fff; font-size: 3.4px; line-height: 20px; text-align: center; }

  /* step 2 */
  .details { left: 407px; top: 110px; width: 321px; height: 234px; background: linear-gradient(180deg, #1a2452 0%, #222f68 60%, #26336d 78%); }
  .details-under { left: 0; top: 181px; width: 321px; height: 53px; background: #6a6a6a; }
  .dim-btn { position: absolute; width: 14px; height: 14px; border: .8px solid rgba(255,255,255,.3); border-radius: 3px; }
  .dim-btn svg { width: 100%; height: 100%; display: block; }
  .modal { position: absolute; left: 23px; top: 57px; width: 277px; height: 136px; background: radial-gradient(ellipse at 40% 60%, #4f62ac 0%, var(--brand) 70%); }
  .modal-title { position: absolute; top: 16px; font-family: "Montserrat", sans-serif; font-weight: 700; font-size: 12px; color: #fff; }
  .field.light { background: #f2f3f8; }
  .area { height: 22px; line-height: 8px; padding-top: 2px; }

  /* step 3 */
  .thanks { left: 407px; top: 402px; width: 321px; height: 188px; background: #ebebeb; }
  .thanks-title { position: absolute; top: 96px; font-family: "Montserrat", sans-serif; font-weight: 700; font-size: 15px; color: var(--brand); }
  .thanks-copy { position: absolute; top: 114px; font-family: "Montserrat", sans-serif; font-weight: 400; font-size: 7.6px; color: #444; }
  .order-number { position: absolute; left: 89px; top: 138px; width: 142px; height: 30px; background: var(--brand-deep); color: #fff; font-family: "Montserrat", sans-serif; font-size: 8.3px; line-height: 30px; text-align: center; }
</style>
</head>
<body>

<div class="step-label" style="left:130px;top:18px;">STEP 1</div>
<div class="step-label" style="left:498px;top:56px;">STEP 2</div>
<div class="step-label" style="left:497px;top:359px;">STEP 3</div>

<!-- STEP 1: landing page -->
<section class="panel home">

  <header class="abs hero" role="img" aria-label="Blue-tinted photo of an industrial caster wheel behind the quote form">
    <span class="icon-btn" style="left:40px;top:12px;"><svg viewBox="0 0 14 14"><path d="M4.5 5.5h5M4.5 7h5M4.5 8.5h5" stroke="#fff" stroke-width=".8"/></svg></span>
    <span class="icon-btn" style="left:246px;top:12px;"><svg viewBox="0 0 14 14"><path d="M5 4.6c.4-.3.8-.2 1 .2l.5 1c.1.3 0 .5-.2.7l-.3.3c.3.7.8 1.2 1.5 1.5l.3-.3c.2-.2.4-.3.7-.2l1 .5c.4.2.5.6.2 1l-.4.4c-.4.4-1 .5-1.6.2-1.3-.6-2.4-1.7-3-3-.3-.6-.2-1.2.2-1.6z" fill="#fff"/></svg></span>
    <span class="icon-btn" style="left:266px;top:12px;"><svg viewBox="0 0 14 14"><circle cx="7" cy="5.6" r="1.5" fill="#fff"/><path d="M4.4 9.6c.3-1.4 1.3-2.1 2.6-2.1s2.3.7 2.6 2.1z" fill="#fff"/></svg></span>
    <span class="brand-dot" style="left:151px;top:9px;width:20px;height:20px;"></span>
    <span class="brand-name center" style="top:34px;">PIVOTS &amp; TREADS .com</span>

    <div class="hero-kicker center">PIVOTS &amp; TREADS .COM</div>
    <h1 class="hero-title center">REQUEST A QUOTE HERE</h1>
    <svg class="abs" style="left:0;top:0;" width="321" height="181" viewBox="0 0 321 181">
      <path d="M75 99H46v43h229V99h-29" fill="none" stroke="#fff" stroke-width=".9"/>
    </svg>
    <div class="field select" style="left:54px;top:114px;width:64px;">Manufacturer Name</div>
    <div class="field select" style="left:121px;top:114px;width:63px;">Manufacturers Part</div>
    <div class="field select" style="left:187px;top:114px;width:37px;">Quantity</div>
    <div class="btn-bright" style="left:228px;top:114px;width:38px;">REQUEST<svg viewBox="0 0 9 3"><path d="M0 1.5h8.4M7 .3l1.4 1.2L7 2.7" stroke="#fff" stroke-width=".5" fill="none"/></svg></div>
  </header>

  <section>
    <div class="abs about-photo" role="img" aria-label="Photo of a grinder throwing sparks in a workshop, fading into white"></div>
    <h2 class="section-title" style="left:155px;top:206px;">ABOUT<br>PIVOTS &amp; TREADS .COM</h2>
    <p class="copy" style="left:156px;top:232px;width:128px;">Lorem ipsum dolor sit amet, consectetur adipiscing elit, sed do eiusmod tempor incididunt ut labore et dolore magna aliqua. Quis ipsum suspendisse ultrices gravida. Risus commodo vive rra maecenas accumsan lacus vel facilisis.</p>
    <p class="copy" style="left:156px;top:256px;width:128px;">Lorem ipsum dolor sit amet, consectetur adipiscing elit, sed do eiusmod tempor incididunt ut labore et dolore magna aliqua. Quis ipsum suspendisse ultrices gravida. Risus commodo vive rra maecenas accumsan lacus vel facilisis.</p>
    <span class="btn-navy" style="left:156px;top:280px;width:42px;">READ MORE</span>
  </section>

  <section class="abs looking">
    <h2 class="section-title" style="left:41px;top:32px;">LOOKING FOR<br>CASTORS &amp; WHEELS?</h2>
    <span class="btn-navy" style="left:41px;top:59px;width:48px;">REQUEST NOW</span>
    <span class="btn-blue" style="left:92px;top:59px;width:62px;">CATALOG DOWNLOAD</span>
    <p class="copy" style="left:167px;top:35px;width:128px;">Lorem ipsum dolor sit amet, consectetur adipiscing elit, sed do eiusmod tempor incididunt ut labore et dolore magna aliqua. Quis ipsum suspendisse ultrices gravida. Risus commodo vive rra maecenas accumsan lacus vel facilisis.</p>
    <p class="copy" style="left:167px;top:59px;width:128px;">Lorem ipsum dolor sit amet, consectetur adipiscing elit, sed do eiusmod tempor incididunt ut labore et dolore magna aliqua. Quis ipsum suspendisse ultrices gravida. Risus commodo vive rra maecenas accumsan lacus vel facilisis.</p>
  </section>

  <section class="abs steps" role="img" aria-label="Blue-tinted caster photo behind the three quote steps">
    <div class="steps-kicker center">#1 SOLUTIONS FOR ALL YOUR APPLICATIONS</div>
    <h2 class="steps-title center">REQUEST QUOTE IT IS EASY AS 1-2-3 STEPS</h2>
    <svg class="abs" style="left:0;top:0;" width="321" height="138" viewBox="0 0 321 138" font-family="Montserrat, sans-serif">
      <g fill="none" stroke="#fff" stroke-width=".6">
        <circle cx="78" cy="86" r="31"/>
        <circle cx="168" cy="86" r="31"/>
        <circle cx="255" cy="86" r="31"/>
      </g>
      <g fill="none" stroke="#fff" stroke-width=".6" font-size="42" font-weight="300">
        <text x="30" y="102">1</text>
        <text x="115" y="102">2</text>
        <text x="203" y="102">3</text>
      </g>
      <g fill="none" stroke="#fff" stroke-width=".6">
        <rect x="72" y="62" width="10" height="12" rx=".8"/>
        <path d="M74 65h1l.6.6M74 68h1l.6.6M74 71h1l.6.6M77 65.5h3M77 68.5h3M77 71.5h3M84 63v10"/>
        <path d="M162 68l6-5 6 5v8h-12z M162 68l6 4 6-4"/>
        <circle cx="168" cy="67" r="1.6"/>
        <rect x="250" y="62" width="12" height="11"/>
        <path d="M254 62v4h4v-4"/>
        <circle cx="261" cy="72" r="3"/>
        <path d="M259.6 72l1 1 1.8-1.8"/>
      </g>
      <g fill="#fff" font-weight="600" font-size="4.4" text-anchor="middle">
        <text x="78" y="85">REQUEST A</text><text x="78" y="91">QUOTE</text>
        <text x="168" y="85">RECEIVE A</text><text x="168" y="91">QUOTE</text>
        <text x="256" y="85">CONVERT A</text><text x="256" y="91">QUOTE TO ORDER</text>
      </g>
      <g fill="#fff" font-family="Poppins, sans-serif" font-size="3" text-anchor="middle">
        <text x="78" y="97">Lorem ipsum dolor sit amet,</text><text x="78" y="100.8">onsectetur adipiscine</text>
        <text x="168" y="97">Lorem ipsum dolor sit amet,</text><text x="168" y="100.8">onsectetur adipiscine</text>
        <text x="256" y="97">Lorem ipsum dolor sit amet,</text><text x="256" y="100.8">onsectetur adipiscine</text>
      </g>
    </svg>
  </section>

  <section>
    <h2 class="products-title center">OUR PRODUCTS</h2>
    <p class="products-copy">Lorem ipsum dolor sit amet, consectetur adipiscing elit, sed do eiusmod tempor incididunt ut labore et dolore magna aliqua. Quis ipsum suspendisse ultrices gravida.</p>

    <article class="card" style="left:40px;top:622px;"><div class="card-photo" role="img" aria-label="Photo of a dark cast iron wheel"></div><div class="card-name">Product Name</div><div class="card-meta">Wheel Material</div></article>
    <article class="card" style="left:102px;top:622px;"><div class="card-photo" role="img" aria-label="Photo of a swivel caster with navy wheel"></div><div class="card-name">Product Name</div><div class="card-meta">Wheel Material</div></article>
    <article class="card" style="left:163px;top:622px;"><div class="card-photo" role="img" aria-label="Photo of three grey wheels in a row"></div><div class="card-name">Product Name</div><div class="card-meta">Wheel Material</div></article>
    <article class="card" style="left:225px;top:622px;"><div class="card-photo" role="img" aria-label="Photo of a plate-mount caster"></div><div class="card-name">Product Name</div><div class="card-meta">Wheel Material</div></article>
    <article class="card" style="left:40px;top:701px;"><div class="card-photo" role="img" aria-label="Photo of a stem caster with orange wheel"></div><div class="card-name">Product Name</div><div class="card-meta">Wheel Material</div></article>
    <article class="card" style="left:102px;top:701px;"><div class="card-photo" role="img" aria-label="Photo of a black swivel caster"></div><div class="card-name">Product Name</div><div class="card-meta">Wheel Material</div></article>
    <article class="card" style="left:163px;top:701px;"><div class="card-photo" role="img" aria-label="Photo of a heavy rigid caster"></div><div class="card-name">Product Name</div><div class="card-meta">Wheel Material</div></article>
    <article class="card" style="left:225px;top:701px;"><div class="card-photo" role="img" aria-label="Photo of a grey caster with blue bracket"></div><div class="card-name">Product Name</div><div class="card-meta">Wheel Material</div></article>
  </section>

  <section>
    <h2 class="services-title center">OUR SERVICES</h2>
    <div class="service-photo" style="left:6px;background:linear-gradient(160deg,#5d5f63,#3b3c40 55%,#b9773a 100%);" role="img" aria-label="Photo of a grinder cutting metal with sparks"></div>
    <div class="service-photo" style="left:112px;background:linear-gradient(160deg,#8b8e92,#5e6166 50%,#9c9fa3);" role="img" aria-label="Photo of a large caster wheel close-up"></div>
    <div class="service-photo" style="left:217px;background:linear-gradient(160deg,#a6a9ab,#6f7376 50%,#8e5a3a);" role="img" aria-label="Photo of a technician in a factory"></div>
    <h3 class="service-name" style="left:6px;">Industrial casters</h3>
    <h3 class="service-name" style="left:112px;">Wheels by OEM's</h3>
    <h3 class="service-name" style="left:217px;">Maintenance</h3>
    <p class="service-copy" style="left:6px;">Lorem ipsum dolor sit amet, con<br>secsit amet consectetur</p>
    <p class="service-copy" style="left:112px;">Lorem ipsum dolor sit amet, con<br>secsit amet consectetur</p>
    <p class="service-copy" style="left:217px;">Lorem ipsum dolor sit amet, con<br>secsit amet consectetur</p>
  </section>

  <footer class="abs footer">
    <span class="brand-dot" style="left:50px;top:30px;width:32px;height:32px;background:var(--brand);"></span>
    <span class="brand-name" style="left:23px;top:70px;color:var(--brand);font-size:6.8px;">PIVOTS &amp; TREADS .com</span>

    <h4 class="foot-head" style="left:119px;">Links</h4>
    <ul class="foot-links">
      <li>Home</li><li>About</li><li>Shop</li><li>Products</li><li>My Account</li><li>Shipping &amp; Delivery</li><li>FAQ's</li>
    </ul>

    <h4 class="foot-head" style="left:169px;">Contact Us</h4>
    <span class="foot-pin" style="left:168px;top:42px;"><svg viewBox="0 0 10 10"><path d="M5 2.4a1.8 1.8 0 0 1 1.8 1.8C6.8 5.6 5 7.6 5 7.6S3.2 5.6 3.2 4.2A1.8 1.8 0 0 1 5 2.4z" fill="#fff"/><circle cx="5" cy="4.2" r=".6" fill="var(--brand)"/></svg></span>
    <p class="foot-line" style="left:181px;top:41px;">Location Name<br>Dummy addess line<br>Riverton 1180 NW (0000)</p>
    <span class="foot-pin" style="left:168px;top:61px;"><svg viewBox="0 0 10 10"><path d="M3.8 3c.3-.2.6-.2.7.1l.4.7c.1.2 0 .4-.1.5l-.2.2c.2.5.6.9 1.1 1.1l.2-.2c.1-.1.3-.2.5-.1l.7.4c.3.1.3.4.1.7l-.3.3c-.3.3-.7.3-1.1.1-.9-.4-1.7-1.2-2.1-2.1-.2-.4-.1-.8.1-1.1z" fill="#fff"/></svg></span>
    <p class="foot-line" style="left:181px;top:64px;">Phone:555.010.0199</p>
    <span class="foot-pin" style="left:168px;top:75px;"><svg viewBox="0 0 10 10"><rect x="3" y="3.6" width="4" height="2.9" fill="#fff"/><path d="M3 3.7l2 1.5 2-1.5" stroke="var(--brand)" stroke-width=".4" fill="none"/></svg></span>
    <p class="foot-line" style="left:180px;top:78px;">Email hello@pivotstreads.example</p>

    <h4 class="foot-head" style="left:236px;">Newsletter Sign up</h4>
    <p class="foot-line" style="left:236px;top:40px;width:66px;line-height:4.2px;">Lorem ipsum dolor sit amelor conse ctet ur adipisciorem ipsumilit,</p>
    <div class="newsletter">Email<svg viewBox="0 0 10 10"><circle cx="5" cy="5" r="4.6" fill="var(--brand)"/><path d="M2.6 5h4.6M5.6 3.5L7.2 5 5.6 6.5" stroke="#fff" stroke-width=".6" fill="none"/></svg></div>
    <span class="social" style="left:239px;"></span>
    <span class="social" style="left:251px;"></span>
    <span class="social" style="left:263px;"></span>
    <span class="social" style="left:275px;"></span>
  </footer>
  <div class="abs legal">© 2022 All Rights Reserved.Terms &amp; Conditions Privacy Policy</div>
</section>

<!-- STEP 2: client details -->
<section class="panel details" role="img" aria-label="Darkened caster photo behind the client details form">
  <span class="dim-btn" style="left:40px;top:13px;"><svg viewBox="0 0 14 14"><path d="M4.5 5.5h5M4.5 7h5M4.5 8.5h5" stroke="rgba(255,255,255,.4)" stroke-width=".8"/></svg></span>
  <span class="dim-btn" style="left:246px;top:13px;"><svg viewBox="0 0 14 14"><path d="M5 4.6c.4-.3.8-.2 1 .2l.5 1c.1.3 0 .5-.2.7l-.3.3c.3.7.8 1.2 1.5 1.5l.3-.3c.2-.2.4-.3.7-.2l1 .5c.4.2.5.6.2 1l-.4.4c-.4.4-1 .5-1.6.2-1.3-.6-2.4-1.7-3-3-.3-.6-.2-1.2.2-1.6z" fill="rgba(255,255,255,.4)"/></svg></span>
  <span class="dim-btn" style="left:266px;top:13px;"><svg viewBox="0 0 14 14"><circle cx="7" cy="5.6" r="1.5" fill="rgba(255,255,255,.4)"/><path d="M4.4 9.6c.3-1.4 1.3-2.1 2.6-2.1s2.3.7 2.6 2.1z" fill="rgba(255,255,255,.4)"/></svg></span>
  <span class="brand-dot" style="left:150px;top:8px;width:20px;height:20px;background:#6e7380;"></span>
  <span class="brand-name center" style="top:35px;color:#6e7380;">PIVOTS &amp; TREADS .com</span>

  <div class="abs details-under"></div>
  <h2 class="section-title" style="left:154px;top:205px;color:var(--night);">ABOUT<br>PIVOTS &amp; TREADS .COM</h2>

  <form class="modal">
    <h2 class="modal-title center">CLIENT DETAILS</h2>
    <svg class="abs" style="left:0;top:0;" width="277" height="136" viewBox="0 0 277 136">
      <path d="M83 24H23v88h227V24h-58" fill="none" stroke="#fff" stroke-width=".9"/>
    </svg>
    <div class="field light" style="left:40px;top:41px;width:64px;">First name</div>
    <div class="field light" style="left:107px;top:41px;width:63px;">Last name</div>
    <div class="field light" style="left:172px;top:41px;width:63px;">Email Address</div>
    <div class="field light area" style="left:40px;top:58px;width:197px;">Optional questions</div>
    <div class="field light" style="left:40px;top:84px;width:64px;">Company name</div>
    <div class="field light" style="left:107px;top:84px;width:85px;">Contact number</div>
    <div class="btn-bright" style="left:194px;top:84px;width:42px;">SUBMIT<svg viewBox="0 0 9 3"><path d="M0 1.5h8.4M7 .3l1.4 1.2L7 2.7" stroke="#fff" stroke-width=".5" fill="none"/></svg></div>
  </form>
</section>

<!-- STEP 3: confirmation -->
<section class="panel thanks">
  <span class="brand-dot" style="left:150px;top:6px;width:22px;height:22px;background:var(--brand);"></span>
  <span class="brand-name center" style="top:34px;color:var(--brand);">PIVOTS &amp; TREADS .com</span>
  <svg class="abs" style="left:148px;top:71px;" width="24" height="24" viewBox="0 0 24 24">
    <circle cx="12" cy="12" r="12" fill="var(--ok)"/>
    <path d="M6.8 12.2l3.4 3.4 7-7" stroke="#fff" stroke-width="2.4" fill="none" stroke-linecap="round" stroke-linejoin="round"/>
  </svg>
  <h2 class="thanks-title center">THANK YOU!</h2>
  <p class="thanks-copy center">Thank you, Your order has been received</p>
  <div class="order-number">Your Order number is 7878</div>
</section>

</body>
</html>
```